Animal Eye Clinic needs a Business card

We are a new veterinary ophthalmology practice (Tessaly Animal Eye Care) and we need a business card designed. We only see animal eyes - we are not a regular veterinary clinic. We already have a logo. We are looking for a professional, good looking business card to hand out to our clients. We are looking for something simple but professional and contemporary. Our logo is likely the only picture/graphic that needs to be on the card.
Updates

Contact Information for Business Card

Marisol Dunkley, BSc, DVM, MSc, DipACVO
Veterinary Ophthalmologist

Phone: 250.418.3097
Email: tessalyanimaleyecare@mailbrook.net
Website: tessalyanimaleyecare.net
Address: 1840 Pellworth Rd
Kelowna, BC, V4T 8M3

Colors

Designer to choose colors to be used in the design.

Requirements
Must have
• Our logo (attached)

```html
<!DOCTYPE html>
<html lang="en">
<head>
<meta charset="utf-8">
<title>Tessaly Animal Eye Care – Business Card</title>
<link href="https://fonts.googleapis.com/css2?family=Open+Sans:wght@400&family=Roboto:wght@500;700&display=swap" rel="stylesheet">
<style>
  :root {
    --teal: #1f9aa8;
    --teal-faint: #e9f5f6;
    --ink: #4a4a4c;
    --text: #3d3d3f;
    --rule: #8a8a8a;
    --paper: #ffffff;
    --backdrop: #8b6b4a;
  }
  html, body {
    margin: 0;
    width: 900px;
    height: 1200px;
    overflow: hidden;
    background: var(--backdrop);
  }
  .canvas { position: relative; width: 900px; height: 1200px; }
  .card {
    position: absolute;
    left: 86px;
    width: 736px;
    height: 430px;
    border-radius: 22px;
    overflow: hidden;
    box-shadow: 0 6px 14px rgba(0,0,0,.35);
  }
  .card-band {
    position: absolute; left: 0; right: 0; bottom: 0; height: 8px;
    background: var(--teal);
  }
  .card-front { top: 137px; background: var(--paper); }
  .card-back { top: 633px; background: var(--ink); }

  .brand {
    position: absolute;
    display: flex;
    align-items: center;
    font-family: "Roboto", sans-serif;
    font-weight: 500;
    color: var(--teal);
    text-transform: uppercase;
  }
  .brand-dot { border-radius: 50%; background: var(--teal); flex: none; }
  .brand-name { line-height: 1.15; }

  .card-front .brand { right: 54px; top: 48px; gap: 20px; }
  .card-front .brand-dot { width: 76px; height: 76px; }
  .card-front .brand-name { font-size: 24px; letter-spacing: .5px; }

  .watermark {
    position: absolute; left: 536px; top: 245px;
    width: 138px; height: 138px; border-radius: 50%;
    background: var(--teal-faint);
  }

  .person { position: absolute; left: 50px; top: 240px; }
  .person-name {
    margin: 0;
    font-family: "Roboto", sans-serif; font-weight: 700;
    font-size: 29px; line-height: 32px; color: var(--teal);
  }
  .person-role {
    margin: 2px 0 0;
    font-family: "Open Sans", sans-serif; font-size: 15px;
    line-height: 19px; color: var(--text); letter-spacing: .3px;
  }
  .rule {
    position: absolute; left: 50px; right: 54px; top: 316px;
    height: 2px; background: var(--rule);
  }
  .contact, .address {
    position: absolute; top: 333px; margin: 0; padding: 0; list-style: none;
    font-family: "Open Sans", sans-serif; font-size: 16px; line-height: 23.5px;
    color: var(--text);
  }
  .contact { left: 50px; }
  .contact li { display: flex; align-items: center; gap: 13px; }
  .contact svg { width: 15px; height: 15px; flex: none; }
  .address { right: 54px; top: 356px; text-align: right; letter-spacing: .3px; }

  .card-back .brand { left: 91px; top: 149px; gap: 30px; }
  .card-back .brand-dot { width: 132px; height: 132px; }
  .card-back .brand-name { font-size: 40px; letter-spacing: 1px; }

  .back-url {
    position: absolute; left: 0; right: 0; top: 378px; margin: 0;
    text-align: center; font-family: "Open Sans", sans-serif; font-size: 15px;
    color: #ffffff;
  }
  .back-url span { color: var(--teal); }
</style>
</head>
<body>
<main class="canvas">

  <section class="card card-front">
    <div class="brand">
      <span class="brand-dot"></span>
      <span class="brand-name">Tessaly<br>Animal Eye Care</span>
    </div>

    <div class="watermark"></div>

    <div class="person">
      <h1 class="person-name">MARISOL DUNKLEY</h1>
      <p class="person-role">BSc, DVM, MSc, DipACVO<br>Veterinary Ophthalmologist</p>
    </div>

    <div class="rule"></div>

    <ul class="contact">
      <li>
        <svg viewBox="0 0 16 16"><path fill="#1f9aa8" d="M3.6 1.2l2.3 2.4-1.2 1.8c.9 2 2.8 3.9 4.9 4.9l1.8-1.2 2.4 2.3-1.6 2.4C7.5 13.3 2.6 8.5 1.2 3.1z"/></svg>
        250.418.3097
      </li>
      <li>
        <svg viewBox="0 0 16 16"><rect x="1.5" y="3.5" width="13" height="9" fill="none" stroke="#1f9aa8" stroke-width="1.4"/><path d="M1.5 3.8L8 9l6.5-5.2" fill="none" stroke="#1f9aa8" stroke-width="1.4"/></svg>
        tessalyanimaleyecare@mailbrook.net
      </li>
      <li>
        <svg viewBox="0 0 16 16" fill="none" stroke="#1f9aa8" stroke-width="1.3"><circle cx="8" cy="8" r="6.3"/><ellipse cx="8" cy="8" rx="2.8" ry="6.3"/><path d="M1.7 8h12.6M2.8 4.8h10.4M2.8 11.2h10.4"/></svg>
        tessalyanimaleyecare.net
      </li>
    </ul>

    <p class="address">1840 Pellworth Rd<br>Kelowna, BC, V4T 8M3</p>

    <div class="card-band"></div>
  </section>

  <section class="card card-back">
    <div class="brand">
      <span class="brand-dot"></span>
      <span class="brand-name">Tessaly<br>Animal Eye Care</span>
    </div>
    <p class="back-url">www.<span>tessalyanimaleyecare</span>.net</p>
    <div class="card-band"></div>
  </section>

</main>
</body>
</html>
```